Fishing charter business in Sitka Alaska needs new business card design

I have had the same design for 10 plus years, ready for something different. I have attached a copy of my current card and my website link is www.bluecoveangling.net
I am looking for something that will catch my clients eye, although I rely on word of mouth for most of my business a a nice business card will help people remember who I am. My business is located in Sitka Alaska, there are probably 20-30 other charter businesses in Sitka. I like the way my current card is laid out, with the two tone black and grey. I can leave it up to the designers to come up with something else.
Target Market(s)
men, women, couples. Anyone who likes fishing
Industry/Entity Type
Tourism
Contact Information for Business Card
Dorrance's Charter Service
Tidewater Rockline Sportfishing
Colors
Designer to choose colors to be used in the design.
Requirements
Must have
- Gilbert Dorrance
- PO Box 4716
- Sitka, AK 99835
- Compass Rose image
- 100 Ton USCG Licensed Captain
- gdorrance@wavelink.net
- 907-555-0142
- www.bluecoveangling.net
Nice to have
- ghost image of "boat helm"
Should not have
- be to complex

```html
<!DOCTYPE html>
<html lang="en">
<head>
<meta charset="utf-8">
<title>Dorrance's Charter Service – Business Card</title>
<link href="https://fonts.googleapis.com/css2?family=Lato:wght@400;700&family=PT+Sans:wght@400;700&display=swap" rel="stylesheet">
<style>
  :root {
    --stage: #666666;
    --card-white: #ffffff;
    --brand-blue: #2b46a8;
    --brand-blue-light: #5a72c0;
    --back-blue: #2e4ca6;
    --ghost-blue: #3a57ae;
    --ghost-blue-light: #4562b6;
    --text-gray: #555555;
    --tag-gray: #6b6b6b;
    --white: #ffffff;
  }
  * { margin: 0; padding: 0; box-sizing: border-box; }
  html, body {
    width: 1200px; height: 900px; overflow: hidden;
    background: var(--stage);
  }
  .stage { position: relative; width: 1200px; height: 900px; }

  .card {
    position: absolute; top: 200px;
    width: 310px; height: 502px;
    box-shadow: 3px 4px 6px rgba(0,0,0,0.45);
    overflow: hidden;
  }
  .card--front {
    left: 253px; background: var(--card-white);
    border-radius: 52px 0 52px 0;
  }
  .card--back {
    left: 627px; background: var(--back-blue);
    border-radius: 0 52px 0 52px;
  }

  .compass-rose {
    position: absolute; left: 95px; top: 84px;
    width: 122px; height: 122px; border-radius: 50%;
    background: radial-gradient(circle, var(--brand-blue-light) 0%, var(--brand-blue) 60%, var(--brand-blue) 100%);
    box-shadow: 0 0 0 5px var(--card-white), 0 0 0 7px var(--brand-blue);
  }

  .brand { position: absolute; left: 0; width: 100%; text-align: center; }
  .brand__name {
    font-family: "PT Sans", sans-serif; font-weight: 700;
    font-size: 18px; letter-spacing: 0.4px; text-transform: uppercase;
    white-space: nowrap;
  }
  .brand__tag {
    font-family: "PT Sans", sans-serif; font-weight: 400;
    font-size: 12px; letter-spacing: 1px; text-transform: uppercase;
    margin-top: 1px; white-space: nowrap;
  }
  .card--front .brand { top: 233px; }
  .card--front .brand__name { color: var(--brand-blue); }
  .card--front .brand__tag { color: var(--tag-gray); }
  .card--back .brand { top: 416px; }
  .card--back .brand__name, .card--back .brand__tag { color: var(--white); }

  .contact {
    position: absolute; left: 33px; top: 313px;
    font-family: "Lato", sans-serif; font-size: 14.5px;
    color: var(--text-gray); line-height: 19px;
  }
  .contact__name {
    font-family: "PT Sans", sans-serif; font-weight: 700;
    font-size: 17px; color: var(--brand-blue); text-transform: uppercase;
    letter-spacing: 0.4px; line-height: 20px;
  }
  .contact__address { margin-top: 8px; }
  .contact__list { list-style: none; margin-top: 8px; }
  .contact__list li { display: flex; align-items: center; gap: 4px; height: 18px; }
  .contact__icon { width: 12px; height: 12px; fill: var(--brand-blue); flex: none; }

  .helm-ghost {
    position: absolute; left: 10px; top: 105px;
    width: 290px; height: 290px; border-radius: 50%;
    background: radial-gradient(circle, var(--ghost-blue-light) 0%, var(--ghost-blue) 45%, var(--back-blue) 58%, var(--ghost-blue) 62%, var(--ghost-blue) 100%);
    border: 2px solid var(--ghost-blue-light);
  }
</style>
</head>
<body>
<main class="stage">

  <section class="card card--front">
    <div class="compass-rose" role="img" aria-label="Compass rose illustration with N, E, S, W points"></div>

    <div class="brand">
      <p class="brand__name">Dorrance's Charter Service</p>
      <p class="brand__tag">Tidewater Rockline Sportfishing</p>
    </div>

    <div class="contact">
      <p class="contact__name">Gilbert Dorrance</p>
      <p class="contact__role">100 Ton USCG Licensed Captain</p>
      <p class="contact__address">PO Box 4716<br>Sitka, AK 99835</p>
      <ul class="contact__list">
        <li>
          <svg class="contact__icon" viewBox="0 0 12 12" aria-hidden="true"><path d="M1 4c0-2 2-3 5-3s5 1 5 3v1H8.5V3.8H3.5V5H1z"/><path d="M3 6h6l1.5 4.5h-9z"/></svg>
          907-555-0142
        </li>
        <li>
          <svg class="contact__icon" viewBox="0 0 12 12" aria-hidden="true"><path d="M1 2.5h10v7H1z"/><path d="M1.5 3l4.5 3.5L10.5 3" fill="none" stroke="#fff" stroke-width="1"/></svg>
          gdorrance@wavelink.net
        </li>
        <li>
          <svg class="contact__icon" viewBox="0 0 12 12" aria-hidden="true"><circle cx="6" cy="6" r="5.5"/><path d="M0.5 6h11M6 0.5c-2 2-2 9 0 11M6 0.5c2 2 2 9 0 11" fill="none" stroke="#fff" stroke-width="0.9"/></svg>
          www.bluecoveangling.net
        </li>
      </ul>
    </div>
  </section>

  <section class="card card--back">
    <div class="helm-ghost" role="img" aria-label="Faint ghost image of a ship's helm wheel"></div>
    <div class="brand">
      <p class="brand__name">Dorrance's Charter Service</p>
      <p class="brand__tag">Tidewater Rockline Sportfishing</p>
    </div>
  </section>

</main>
</body>
</html>
```